We are a printed circuit board manufacturer. Need a company professional web site to allow our potential customers to know more about our background, capability and our products. The web site will contain three languages, which are Chinese, English and Japanese. Our audience are mainly electronic companies that procure printed circuit boards. I have a word document that have all the required text in all three languages. The final design should communicate the impression that we embrace quality, trustworthiness and long term partnership business principles.
We should have sections that allow us to post pictures of our facilities.
I have added the three files in three different languages.
Some of the information is below:
Background
RVD Worldwide Limited (RVD) was set up in Hong Kong in 2007 by two Hong Kong entrepreneurs, Mr. Lok Fai Tam and Mr. Wai Ho. We acquired the single sided printed circuit board factory located in Dongguan City, Guangdong Province, China, from Valtor Corporation of the U.S. in 2007. In addition to RVD, Mr. Tam and Mr. Ho also own Brightrail Systems Company Limited, a semiconductor company based in Hong Kong since 1997 with a total investment of over US$100 million. Brightrail is engaged in the manufacturing of flexible substrates and MEMS assembly business.
RVD has been awarded TS 16949 and ISO14000 certificates since 2009 and 2004 respectively.
Business Principles
RVD Worldwide Limited strives to be a professional top notched printed circuit board supplier. We embrace four “EXCELLENCE” principles, namely, excellence in quality, excellence in prices, excellence in services and excellence in on time delivery.
We approach each customer with a long-term partnership view that delivers the lowest ownership costs and highest total values to our customers. We customize quotations and solutions in order to allow our customers to win more businesses. We believe by thinking from our customers’ points of view we will be able to create a WIN-WIN relationship.
Customers
Due to our excellent quality, services and production systems, RVD Worldwide Limited manage to service a number of large Japanese and US customers, which include:
Technical capability overview
Below is an overview of our current capability:
Target Market(s)
Electronic companies buyers
Industry/Entity Type
Business
Requirements
Must have
- Capability description
Should not have
- no cartoon

```html
<!DOCTYPE html>
<html lang="en">
<head>
<meta charset="utf-8">
<title>RVD Worldwide Limited</title>
<link rel="stylesheet" href="https://fonts.googleapis.com/css2?family=Arimo:wght@400;700&display=swap">
<style>
  :root {
    --page-bg: #ffffff;
    --band-grey: #eeeded;
    --nav-teal: #3d8f78;
    --nav-teal-light: #4a9c85;
    --nav-active: #16553f;
    --heading-green: #2e7a5e;
    --text-main: #3a3a3a;
    --text-muted: #777777;
    --bullet-grey: #8c8c8c;
    --rule: #e2e2e2;
    --arrow-grey: #b9b9b9;
    --brand-green: #1f6e4e;
  }
  * { box-sizing: border-box; margin: 0; padding: 0; }
  html, body { width: 1200px; height: 1108px; overflow: hidden; }
  body {
    position: relative;
    background: var(--page-bg);
    font-family: "Arimo", Arial, sans-serif;
    color: var(--text-main);
  }
  .top-band { position: absolute; left: 0; top: 0; width: 1200px; height: 7px; background: var(--band-grey); }

  .brand {
    position: absolute; left: 31px; top: 48px;
    display: flex; align-items: center; gap: 12px;
    font-size: 26px; font-weight: 700; color: var(--brand-green); letter-spacing: 0.3px;
  }
  .brand-square { width: 22px; height: 22px; background: var(--brand-green); }

  .main-nav {
    position: absolute; left: 582px; top: 93px; width: 590px; height: 38px;
    display: flex; background: linear-gradient(180deg, var(--nav-teal-light), var(--nav-teal));
  }
  .main-nav a {
    flex: 1; display: flex; align-items: center; justify-content: center;
    color: #fff; text-decoration: none; font-size: 17px;
  }
  .main-nav a.is-active { background: var(--nav-active); }

  .hero {
    position: absolute; left: 29px; top: 134px; width: 1144px; height: 432px;
    background:
      linear-gradient(180deg, rgba(196,199,196,0.85) 0%, rgba(196,199,196,0) 22%),
      linear-gradient(0deg, rgba(196,104,58,0.55) 0%, rgba(196,104,58,0) 16%),
      radial-gradient(ellipse 22% 40% at 68% 78%, rgba(150,180,205,0.75), rgba(150,180,205,0) 100%),
      radial-gradient(ellipse 12% 35% at 11% 65%, rgba(140,165,190,0.6), rgba(140,165,190,0) 100%),
      linear-gradient(90deg, #8e928c 0%, #c6c9c4 14%, #e3e4e0 32%, #eceeea 50%, #dcdedb 64%, #b7ab94 80%, #9c8466 100%);
  }

  .welcome-tab {
    position: absolute; left: 29px; top: 569px; width: 289px; height: 37px;
    background: linear-gradient(180deg, #4a9c85, #2f7f67);
    color: #fff; font-size: 21px; padding: 6px 0 0 18px;
  }
  .intro {
    position: absolute; left: 47px; top: 622px; width: 690px;
    font-size: 14.6px; line-height: 20px; color: var(--text-main);
  }
  .read-more {
    position: absolute; font-size: 11.5px; color: var(--text-muted);
    text-transform: uppercase; letter-spacing: 0.2px;
  }
  .read-more.about { left: 664px; top: 758px; }
  .read-more.services { left: 1085px; top: 758px; }

  .section-title { position: absolute; font-size: 19px; font-weight: 400; color: var(--heading-green); }
  .section-title.services { left: 799px; top: 581px; }
  .section-title.gallery { left: 48px; top: 798px; }
  .section-title.clients { left: 795px; top: 798px; }

  .service-list { position: absolute; left: 803px; top: 621px; list-style: none; }
  .service-list li {
    display: flex; align-items: center; gap: 10px;
    font-size: 14.8px; height: 25.6px; color: var(--text-main);
  }
  .service-list li::before { content: ""; width: 9px; height: 9px; background: var(--bullet-grey); }

  .divider { position: absolute; left: 29px; top: 787px; width: 1144px; height: 1px; background: var(--rule); }

  .gallery-arrow { position: absolute; top: 896px; width: 16px; height: 26px; }
  .gallery-arrow.prev { left: 40px; }
  .gallery-arrow.next { left: 709px; }
  .thumb { position: absolute; top: 847px; width: 176px; height: 123px; }
  .thumb.one { left: 65px; background: linear-gradient(135deg, #9ea39d, #dfe1dc 55%, #7f8580); }
  .thumb.two { left: 292px; background: linear-gradient(135deg, #c9ccc5, #c9622e 50%, #8b8e88); }
  .thumb.three { left: 519px; background: linear-gradient(135deg, #3e6b46, #d8dad5 45%, #a9aca6); }

  .clients-line { position: absolute; left: 799px; top: 838px; font-size: 14.8px; color: var(--text-main); }
  .client-name {
    position: absolute; top: 906px; width: 170px;
    display: flex; align-items: center; justify-content: center; gap: 10px;
    font-size: 26px; font-weight: 700; color: var(--text-main);
  }
  .client-name.first { left: 781px; }
  .client-name.second { left: 978px; }
  .client-square { width: 16px; height: 16px; background: var(--text-main); }

  .site-footer {
    position: absolute; left: 0; top: 999px; width: 1200px; height: 109px;
    background: var(--band-grey);
  }
  .site-footer p {
    position: absolute; left: 0; top: 50px; width: 1202px; text-align: center;
    font-size: 12px; color: #555; text-transform: uppercase;
  }
</style>
</head>
<body>
  <div class="top-band"></div>

  <div class="brand"><span class="brand-square"></span>RVD Worldwide Limited</div>

  <nav class="main-nav">
    <a class="is-active" href="#">Home</a>
    <a href="#">About us</a>
    <a href="#">Services</a>
    <a href="#">Gallery</a>
    <a href="#">Contact us</a>
  </nav>

  <div class="hero" role="img" aria-label="Factory floor with engineers testing white electrical control cabinets beside an orange workbench"></div>

  <div class="welcome-tab">Welcome to our website!</div>
  <p class="intro">RVD Worldwide Limited (RVD) was set up in Hong Kong in 2007 by two Hong Kong entrepreneurs, Mr. Lok Fai Tam and Mr. Wai Ho.&nbsp; We acquired the single sided printed circuit board factory located in Dongguan City, Guangdong Province, China, from Valtor Corporation of the U.S. in 2007. In addition to RVD, Mr. Tam and Mr. Ho also own Brightrail Systems Company Limited, a semiconductor company based in Hong Kong since 1997 with a total investment of over US$100 million.&nbsp; Brightrail is engaged in the manufacturing of flexible substrates and MEMS assembly business.</p>
  <span class="read-more about">Read more</span>

  <h2 class="section-title services">What we do</h2>
  <ul class="service-list">
    <li>Plating</li>
    <li>Printing Processes</li>
    <li>Punching And CNC Process</li>
    <li>Surface Finishing</li>
    <li>Specification for carbon</li>
  </ul>
  <span class="read-more services">Read more</span>

  <div class="divider"></div>

  <h2 class="section-title gallery">Gallery</h2>
  <svg class="gallery-arrow prev" viewBox="0 0 16 26" aria-hidden="true"><path d="M13 3 L4 13 L13 23" fill="none" stroke="var(--arrow-grey)" stroke-width="3.5"/></svg>
  <div class="thumb one" role="img" aria-label="Control cabinet assembly line"></div>
  <div class="thumb two" role="img" aria-label="Orange production machine"></div>
  <div class="thumb three" role="img" aria-label="Worker handling boards at a processing line"></div>
  <svg class="gallery-arrow next" viewBox="0 0 16 26" aria-hidden="true"><path d="M3 3 L12 13 L3 23" fill="none" stroke="var(--arrow-grey)" stroke-width="3.5"/></svg>

  <h2 class="section-title clients">Our Clients</h2>
  <p class="clients-line">Industrial Equipment &amp; Power Suplier</p>
  <div class="client-name first"><span class="client-square"></span>Korvex</div>
  <div class="client-name second">Dalmund</div>

  <footer class="site-footer">
    <p>© 2012&nbsp; - Terms of Service - Privacy Policy - Program Policies</p>
  </footer>
</body>
</html>
```